Harlow Mesa Podiatry
Business card, letterhead & envelope
Professional
4631 NW 52nd St
Suite 310
Summerfield, FL 32786
mtollanddpm@brindlemail.com
Front of Card should also have names of doctors:
Marcus Tolland, DPM
Lanh T. Vu, DPM
Back of card should have information for appointment:
1. Date
2. Time
3. Day of week to circle (ie Mon, Tues, Wed, Thurs, Fri)
4. "If unable to keep appointment kindly give 24 hours notice"
Logo designs for Harlow Mesa Podiatry

```html
<!DOCTYPE html>
<html lang="en">
<head>
<meta charset="utf-8">
<title>Harlow Mesa Podiatry — Stationery</title>
<link href="https://fonts.googleapis.com/css2?family=Montserrat:wght@400;700&display=swap" rel="stylesheet">
<style>
  :root {
    --green: #76b41c;
    --green-dark: #5f9614;
    --green-light: #8cc63a;
    --charcoal: #3b3b3b;
    --paper: #ffffff;
    --ground: #e9eaeb;
    --ink: #555555;
    --faint: #e4e6e2;
  }
  * { margin: 0; padding: 0; box-sizing: border-box; }
  html, body { width: 1200px; height: 725px; overflow: hidden; }
  body {
    background-color: var(--ground);
    background-image:
      linear-gradient(rgba(0,0,0,.035) 1px, transparent 1px),
      linear-gradient(90deg, rgba(0,0,0,.035) 1px, transparent 1px);
    background-size: 6px 6px;
    font-family: "Montserrat", Arial, sans-serif;
    color: var(--ink);
    position: relative;
  }
  .sheet { position: absolute; box-shadow: 0 1px 4px rgba(0,0,0,.25); overflow: hidden; }

  /* Brand name lockup */
  .brand { display: flex; align-items: center; gap: 6px; color: var(--green); font-weight: 700; text-transform: uppercase; line-height: 1; white-space: nowrap; }
  .brand-mark { background: var(--green); flex: none; }

  /* Letterhead */
  .letterhead { left: 137px; top: 12px; width: 295px; height: 696px; background: var(--paper); }
  .letterhead .brand { position: absolute; left: 14px; top: 16px; font-size: 11px; }
  .letterhead .brand-mark { width: 16px; height: 16px; }
  .letterhead-watermark { position: absolute; left: 0; right: 0; top: 210px; text-align: center; color: var(--faint); font-weight: 700; text-transform: uppercase; }
  .letterhead-watermark .square { width: 70px; height: 70px; background: var(--faint); margin: 0 auto 22px; }
  .letterhead-watermark .line1 { font-size: 50px; line-height: 1; }
  .letterhead-watermark .line2 { font-size: 22px; letter-spacing: 6px; font-weight: 400; margin-top: 6px; }
  .letterhead-swoosh { position: absolute; left: 0; bottom: 0; }
  .letterhead-contact { position: absolute; left: 12px; bottom: 20px; font-size: 5px; line-height: 1.5; }
  .letterhead-address { position: absolute; right: 14px; bottom: 20px; font-size: 5px; line-height: 1.5; color: #fff; text-align: right; }

  /* Business cards */
  .card { left: 5px; width: 123px; height: 78px; }
  .card-back { top: 132px; background: var(--charcoal); display: flex; }
  .card-back-side { width: 40px; background: var(--green); padding: 6px 4px; }
  .card-back-side .brand { color: #fff; font-size: 6px; flex-direction: column; align-items: flex-start; gap: 4px; }
  .card-back-side .brand-mark { width: 12px; height: 12px; background: #fff; }
  .appointment { flex: 1; padding: 5px 6px; color: #fff; font-size: 4.5px; }
  .appointment-title { font-weight: 700; margin-bottom: 3px; }
  .appointment-row { display: flex; border-bottom: .5px solid #aaa; height: 9px; align-items: flex-end; padding-bottom: 1px; }
  .appointment-row span { width: 18px; }
  .days { display: flex; justify-content: space-between; margin-top: 4px; }
  .notice { margin-top: 5px; font-size: 3.6px; color: #ddd; }

  .card-front { top: 216px; background: var(--paper); }
  .card-front .brand { position: absolute; left: 6px; top: 8px; font-size: 5.6px; gap: 4px; }
  .card-front .brand-mark { width: 10px; height: 10px; }
  .card-front .doctors { position: absolute; right: 6px; top: 8px; font-size: 3.6px; text-align: right; line-height: 1.5; white-space: nowrap; }
  .card-front .contact { position: absolute; left: 7px; top: 40px; font-size: 3.8px; line-height: 1.5; }
  .card-front .address { position: absolute; right: 6px; bottom: 4px; font-size: 3.8px; line-height: 1.5; color: #fff; text-align: right; }
  .card-front svg { position: absolute; left: 0; bottom: 0; }

  /* Envelope */
  .envelope { left: 449px; top: 149px; width: 744px; height: 216px; background: var(--green); }
  .envelope-flap { position: absolute; left: 0; top: 0; width: 100%; height: 18px; background: var(--green-dark); }
  .envelope-flap-tag { position: absolute; left: 352px; top: 4px; width: 44px; height: 16px; background: var(--paper); }
  .envelope-logo { position: absolute; left: 36px; top: 38px; width: 108px; height: 41px; background: var(--paper); }
  .envelope-logo .brand { position: absolute; left: 8px; top: 11px; font-size: 9px; gap: 5px; }
  .envelope-logo .brand-mark { width: 14px; height: 14px; }
  .envelope-contact { position: absolute; left: 40px; top: 106px; font-size: 5px; line-height: 1.6; color: #fff; }
  .envelope-art { position: absolute; left: 403px; top: 18px; right: 0; bottom: 0; background: linear-gradient(160deg, var(--green) 0%, var(--green-light) 100%); }
  .envelope-window { position: absolute; left: 362px; top: 108px; width: 173px; height: 72px; background: var(--paper); border-radius: 8px; }
</style>
</head>
<body>

  <section class="sheet card card-back" aria-label="Appointment card, back">
    <div class="card-back-side">
      <div class="brand"><span class="brand-mark"></span>Harlow<br>Mesa<br>Podiatry</div>
    </div>
    <div class="appointment">
      <p class="appointment-title">Appointment</p>
      <div class="appointment-row"><span>Date</span></div>
      <div class="appointment-row"><span>Time</span></div>
      <div class="days"><span>Mon</span><span>Tues</span><span>Wed</span><span>Thurs</span><span>Fri</span></div>
      <p class="notice">If unable to keep appointment kindly give 24 hours notice</p>
    </div>
  </section>

  <section class="sheet card card-front" aria-label="Business card, front">
    <div class="brand"><span class="brand-mark"></span>Harlow Mesa<br>Podiatry</div>
    <div class="doctors">Marcus Tolland, DPM<br>Lanh T. Vu, DPM</div>
    <div class="contact">Phone: (352) 555-0148<br>mtollanddpm@brindlemail.com</div>
    <svg width="123" height="40" viewBox="0 0 123 40" aria-hidden="true">
      <path d="M0 40 L0 36 Q70 34 123 2 L123 40 Z" fill="var(--green)"/>
    </svg>
    <div class="address">4631 NW 52nd St, Suite 310<br>Summerfield, FL 32786</div>
  </section>

  <section class="sheet letterhead" aria-label="Letterhead">
    <div class="brand"><span class="brand-mark"></span>Harlow Mesa<br>Podiatry</div>
    <div class="letterhead-watermark" aria-hidden="true">
      <div class="square"></div>
      <div class="line1">Harlow</div>
      <div class="line1">Mesa</div>
      <div class="line2">Podiatry</div>
    </div>
    <svg class="letterhead-swoosh" width="295" height="130" viewBox="0 0 295 130" aria-hidden="true">
      <path d="M0 130 L0 122 Q190 118 295 0 L295 130 Z" fill="var(--green)"/>
    </svg>
    <div class="letterhead-contact">Phone: (352) 555-0148<br>mtollanddpm@brindlemail.com</div>
    <div class="letterhead-address">4631 NW 52nd St, Suite 310<br>Summerfield, FL 32786</div>
  </section>

  <section class="sheet envelope" aria-label="Envelope">
    <div class="envelope-flap"></div>
    <div class="envelope-art" role="img" aria-label="White line drawing of a foot and lower leg"></div>
    <div class="envelope-flap-tag"></div>
    <div class="envelope-logo">
      <div class="brand"><span class="brand-mark"></span>Harlow Mesa<br>Podiatry</div>
    </div>
    <div class="envelope-contact">Phone: (352) 555-0148<br>mtollanddpm@brindlemail.com<br>4631 NW 52nd St, Suite 310<br>Summerfield, FL 32786</div>
    <div class="envelope-window"></div>
  </section>

</body>
</html>
```